Heath Weight Loss Retreat Website

The brief:
PineLoop is a provider of health & weight loss retreats and wish to redesign their main website. The website needs to provide detailed information about the company’s services whilst gathering the maximum number of leads possible. The website does not aim to get clients to ‘book now’ but to request further information, or ask a question generating a lead/opportunity for the business.

Primary objectives of website
• Gather leads for products (not necessarily to book at that point, but to ‘request more info’)
• Provide detailed information about the health and fitness programs on offer

Demographic Considerations
• Target age group: 30-50
• Predominant client base are female but website should be gender neutral due to some men attending

Design considerations
• Essentially selling ‘travel experiences’ and ‘life transformations’ so needs to be lots of images to display (similar to a hotel website for example)
• Images need to display real people – i.e. larger people, rather than super thin
• Not too much use of flash
• SEO friendly (we have good rankings at present)
• Will be implemented into Joomla, so please consider this on the design
• Colours should be ‘warm’ and ‘friendly’ and gender neutral

Project Requirements & Expectations
Please supply your design ideas with:
• At least 1 (preferably more) homepage examples
• At least 1 (preferably more) internal page examples
Once a preferred design has been selected the following will be produced, tweaked and approved:
• Homepage + 1 internal landing page + 1 internal main page + 1 contact page + 1 info request page

Attachments
We have attached both a homepage and internal page example which demonstates the type of content needed and the calls to action. This is for demonstration purposes only so please ignore colours, fonts, etc and provide your best designs based on a general layout as per attached.

Images:
A selection of example images has been attached. For the homepage images of the retreats themselves should be used alongside images of ‘larger people’.

Further information:
Please contact Simon Thackery at simon.thackery@coralbeaconfiles.com.au

Target Market(s)

Overweight females aged 30-50 are the main target market. However must be gender neutral due to some men using product.

Industry/Entity Type

Weight

Requirements
Should not have
• Not too much flash

```html
<!DOCTYPE html>
<html lang="en">
<head>
<meta charset="utf-8">
<title>PineLoop Weight Loss Retreat</title>
<link rel="stylesheet" href="https://fonts.googleapis.com/css2?family=Arimo:wght@400;700&family=Crimson+Text:ital,wght@0,400;0,600;1,400;1,600&display=swap">
<style>
:root{
  --green:#8cc31e;
  --green-dark:#6fa013;
  --green-light:#a9d64a;
  --orange:#f0961a;
  --orange-dark:#d97c0a;
  --navy:#123d5e;
  --text:#333333;
  --muted:#8a8a8a;
  --line:#dcdcdc;
  --page-bg:#eef0ea;
  --white:#ffffff;
}
*{box-sizing:border-box;margin:0;padding:0}
html,body{width:1182px;height:1200px;overflow:hidden}
body{background:var(--page-bg);font-family:"Arimo",Arial,sans-serif;color:var(--text);position:relative}
ul{list-style:none}
a{color:inherit;text-decoration:none}

.side-stripe{position:absolute;top:0;bottom:0;width:6px;background:linear-gradient(var(--green-light),#d8ebb3)}
.side-stripe.left{left:118px}
.side-stripe.right{left:1063px}

.page{position:absolute;left:124px;top:0;width:939px;height:1200px;background:var(--white)}
.abs{position:absolute}

/* top strip */
.top-strip{left:285px;top:0;width:654px;height:21px;background:var(--green);border-radius:0 0 0 18px;color:var(--white);font-size:12px}
.top-strip .phone{position:absolute;left:26px;top:2px;font-family:"Crimson Text",serif;font-size:16px;font-weight:600;letter-spacing:.5px;display:flex;align-items:center;gap:10px}
.top-strip .account{position:absolute;right:14px;top:4px;font-size:11px}

/* brand */
.brand{left:24px;top:54px;display:flex;align-items:center;gap:10px}
.brand-mark{width:14px;height:14px;background:var(--green)}
.brand-name{font-size:34px;font-weight:400;color:var(--text);line-height:1}
.brand-tag{left:48px;top:94px;font-size:11px;color:var(--muted);letter-spacing:.5px}

/* header nav */
.head-col h3{font-family:"Arimo",sans-serif;font-weight:400;color:var(--green-dark);font-size:16px;margin-bottom:8px}
.head-col li{font-size:11.5px;color:#777;line-height:18px;padding-left:14px;position:relative}
.head-col li::before{content:"";position:absolute;left:1px;top:5px;border-left:5px solid var(--green);border-top:4px solid transparent;border-bottom:4px solid transparent}
.free-mag{left:818px;top:28px;width:90px;text-align:center}
.free-mag .free{font-size:24px;color:var(--orange);line-height:1}
.free-mag .mag{font-size:11px;color:#777;margin-top:2px}
.free-mag .cover{width:30px;height:42px;margin:8px auto 6px;background:linear-gradient(#3a6fb7,#d9e6f4)}
.free-mag .req{font-size:12px;font-weight:700;color:#d42020}

/* sidebar menu */
.side-menu{left:12px;top:155px;width:228px;background:#f4f4f4}
.side-menu h2{height:34px;background:linear-gradient(var(--green-light),var(--green-dark));color:var(--white);font-family:"Crimson Text",serif;font-weight:600;font-size:16px;letter-spacing:.6px;padding:7px 12px;text-transform:uppercase}
.side-menu li{height:27px;line-height:27px;padding-left:11px;font-size:11.5px;color:#444;border-bottom:1px solid #e2e2e2;text-transform:uppercase;letter-spacing:.3px}
.side-menu li.current{background:var(--green);color:var(--white);border-bottom-color:var(--green)}

.cta-btn{left:12px;width:228px;height:47px;border-radius:4px;color:var(--white);font-family:"Crimson Text",serif;font-size:25px;padding:6px 16px;display:flex;justify-content:space-between;align-items:center}
.cta-btn.orange{background:linear-gradient(#f6b24a,var(--orange-dark))}
.cta-btn.green{background:linear-gradient(#b4dc59,var(--green-dark))}

/* quick contact */
.quick-contact{left:12px;top:673px;width:228px;height:213px;background:var(--navy);border-radius:4px;padding:9px 15px}
.quick-contact h2{font-family:"Crimson Text",serif;font-weight:400;font-size:26px;color:var(--white);margin-bottom:16px}
.quick-contact .field{background:var(--white);font-size:11px;color:#999;padding:5px 15px;margin-bottom:10px}
.quick-contact .field.email{height:26px}
.quick-contact .field.question{height:74px}
.quick-contact .go{position:absolute;right:16px;bottom:13px;width:56px;height:22px;background:linear-gradient(#fff,#ddd);border-radius:3px;font-weight:700;font-size:13px;color:var(--navy);text-align:center;line-height:22px}

/* hero */
.hero{left:255px;top:155px;width:666px;height:304px;border:3px solid var(--green);overflow:hidden}
.hero > svg{position:absolute;left:0;top:0}
.hero h1{position:absolute;left:376px;top:64px;font-family:"Crimson Text",serif;font-style:italic;font-weight:400;font-size:33px;color:#3a2a10;white-space:nowrap}
.hero p{position:absolute;left:376px;top:112px;width:270px;font-family:"Crimson Text",serif;font-style:italic;font-size:17px;line-height:22px;color:var(--white)}
.hero .more{position:absolute;left:362px;top:231px;width:277px;height:36px;background:linear-gradient(#fff,#e4e4e4);border-radius:5px;font-family:"Crimson Text",serif;font-size:15.5px;letter-spacing:.5px;color:#222;display:flex;align-items:center;justify-content:space-between;padding:0 10px 0 14px}

/* feature cards */
.features{left:255px;top:483px;width:666px;height:119px;display:flex;border:1px solid var(--line)}
.feature{flex:1;position:relative;border-right:1px solid var(--line);background:linear-gradient(#fff,#f1f1f1);padding:6px 8px}
.feature:last-child{border-right:none}
.feature h3{font-family:"Crimson Text",serif;font-weight:400;font-size:19px;line-height:21px;color:var(--green-dark)}
.feature .art{position:absolute;right:6px;bottom:8px;width:64px;height:62px;border-radius:4px}
.feature .go{position:absolute;left:12px;bottom:14px;width:78px;height:22px;background:linear-gradient(#f6b24a,var(--orange-dark));border-radius:3px;color:var(--white);font-size:11.5px;font-weight:700;text-align:center;line-height:22px}

/* body copy */
.intro{left:255px;top:621px;width:666px;font-size:11.2px;line-height:20px;color:var(--muted)}
.intro p{margin-bottom:20px}
.intro p.tight{margin-bottom:0}

/* footer */
.footer-links{left:12px;top:991px;width:909px;height:172px;background:linear-gradient(#f4f4f4,#fbfbfb);border:1px solid var(--line);padding:14px 12px;display:flex}
.footer-col{width:170px}
.footer-col h3{font-weight:400;font-size:15.5px;color:#222;margin-bottom:12px}
.footer-col li{font-size:11.5px;line-height:18px;color:#333;padding-left:22px;position:relative}
.footer-col li::before{content:"";position:absolute;left:10px;top:8px;width:3px;height:3px;background:#333;border-radius:50%}
.footer-col li.plain::before{display:none}
.footer-bar{left:12px;top:1163px;width:909px;height:32px;background:var(--green);color:var(--white);font-size:11px;display:flex;justify-content:space-between;align-items:center;padding:0 12px}
</style>
</head>
<body>
<div class="side-stripe left"></div>
<div class="side-stripe right"></div>

<div class="page">
  <div class="abs top-strip">
    <span class="phone">
      <svg width="14" height="14" viewBox="0 0 24 24" aria-hidden="true"><path fill="#fff" d="M6.6 10.8a15.1 15.1 0 0 0 6.6 6.6l2.2-2.2c.3-.3.7-.4 1-.2 1.1.4 2.3.6 3.6.6.6 0 1 .4 1 1V20c0 .6-.4 1-1 1A17 17 0 0 1 3 4c0-.6.4-1 1-1h3.5c.6 0 1 .4 1 1 0 1.3.2 2.5.6 3.6.1.3 0 .7-.2 1z"/></svg>
      CALL US : 0455 - 2180 - 36417
    </span>
    <span class="account">Log in &nbsp;/&nbsp; Sign Up</span>
  </div>

  <div class="abs brand">
    <span class="brand-mark"></span>
    <span class="brand-name">PineLoop</span>
  </div>
  <div class="abs brand-tag">Weight Loss Retreat</div>

  <nav class="abs head-col" style="left:300px;top:28px">
    <h3>The Best Programs</h3>
    <ul><li>Weight Loss Retreat</li><li>Residential Boot Camp</li><li>Fitness Days</li><li>At home program</li><li>Local group exercise</li></ul>
  </nav>
  <nav class="abs head-col" style="left:470px;top:28px">
    <h3>The Best Locations</h3>
    <ul><li>Blue Mountains, NSW</li><li>Sunshine Coast, QLD</li><li>Local Programs</li></ul>
  </nav>
  <nav class="abs head-col" style="left:638px;top:28px">
    <h3>Act now and get results</h3>
    <ul><li>Why choose PineLoop</li><li>Expert Team</li><li>What clients say...</li><li>Contact us</li><li>FREE Brochure</li></ul>
  </nav>
  <div class="abs free-mag">
    <div class="free">FREE</div>
    <div class="mag">PineLoop Magazine</div>
    <div class="cover" role="img" aria-label="Magazine cover"></div>
    <div class="req">Request now</div>
  </div>

  <nav class="abs side-menu">
    <h2>Weight Loss Retreat</h2>
    <ul>
      <li>Overview</li><li class="current">Program Details</li><li>Available Locations</li><li>Is it suitable for you?</li><li>Typical Day</li><li>Great Food</li><li>Valuable Education</li><li>Lasting Results</li><li>Photo Gallery</li><li>Testimonials</li>
    </ul>
  </nav>

  <a class="abs cta-btn orange" style="top:494px">Dates &amp; Rates <svg width="22" height="26" viewBox="0 0 22 26"><path d="M4 2l14 11L4 24" fill="none" stroke="#fff" stroke-width="5"/></svg></a>
  <a class="abs cta-btn green" style="top:550px">Book Now <svg width="22" height="26" viewBox="0 0 22 26"><path d="M4 2l14 11L4 24" fill="none" stroke="#fff" stroke-width="5"/></svg></a>
  <a class="abs cta-btn green" style="top:605px">Contact us <svg width="22" height="26" viewBox="0 0 22 26"><path d="M4 2l14 11L4 24" fill="none" stroke="#fff" stroke-width="5"/></svg></a>

  <form class="abs quick-contact">
    <h2>Quick Contact</h2>
    <div class="field email">Name Email</div>
    <div class="field question">Question</div>
    <div class="go">GO</div>
  </form>

  <section class="abs hero">
    <svg width="660" height="298" viewBox="0 0 660 298">
      <defs>
        <linearGradient id="photoTone" x1="0" y1="0" x2="0" y2="1"><stop offset="0" stop-color="#eef0f2"/><stop offset="1" stop-color="#c9cfd4"/></linearGradient>
        <linearGradient id="panelTone" x1="0" y1="0" x2="1" y2="0"><stop offset="0" stop-color="#f7a21f"/><stop offset="1" stop-color="#ef8e12"/></linearGradient>
      </defs>
      <rect width="660" height="298" fill="url(#photoTone)" role="img" aria-label="Photo of a relaxed woman meditating on an exercise ball"/>
      <path d="M345 0 C300 70 300 220 350 298 L660 298 L660 0 Z" fill="var(--green)"/>
      <path d="M362 0 C318 70 318 220 368 298 L660 298 L660 0 Z" fill="url(#panelTone)"/>
    </svg>
    <h1>Weight Loss Retreat</h1>
    <p>Lasting weight loss and lifestyle<br>change for people<br>of all ages, shapes, sizes and fitness<br>levels.</p>
    <a class="more"><span>REQUEST MORE INFORMATION</span><svg width="14" height="16" viewBox="0 0 14 16"><path d="M3 2l7 6-7 6" fill="none" stroke="var(--orange)" stroke-width="3.5"/></svg></a>
  </section>

  <section class="abs features">
    <div class="feature"><h3>Download<br>brochure</h3><div class="art" role="img" aria-label="Brochure illustration" style="background:linear-gradient(135deg,#2c5aa0,#e8eef6)"></div><a class="go">Click here</a></div>
    <div class="feature"><h3>Available<br>locations</h3><div class="art" role="img" aria-label="Map and compass illustration" style="background:linear-gradient(135deg,#3b8fd0,#b9d9f0)"></div><a class="go">Click here</a></div>
    <div class="feature"><h3>Dates &amp;<br>Costs</h3><div class="art" role="img" aria-label="Calendar and piggy bank illustration" style="background:linear-gradient(135deg,#6fb3e6,#1f6fb8)"></div><a class="go">Click here</a></div>
    <div class="feature"><h3>What<br>clients say</h3><div class="art" role="img" aria-label="Photo of a smiling client" style="background:linear-gradient(#2a6a86,#163f55)"></div><a class="go">Click here</a></div>
  </section>

  <article class="abs intro">
    <p>Hundreds of people have already transformed their lives with PineLoop's proven programs. With &nbsp;PineLoop you will lose weight, lose centimetres, get fit and experience lasting health and fitness results.</p>
    <p class="tight">Our Weight Loss Retreat program is suitable for people of all ages, shapes, sizes and fitness levels. It is amazingly fun and extremely effective with amazing weight loss and fitness results. Whether you want a kick start or are embarking on a long term weight loss program our Weight Loss Retreat program will be one of the best experiences of your life – that's our promise to you.</p>
    <p class="tight">Hundreds of people have already transformed their lives with PineLoop's proven programs. With PineLoop you will lose weight, lose centimetres, get fit and experience lasting health and fitness</p>
    <p>Hundreds of people have already transformed their lives with PineLoop's proven programs. With &nbsp;PineLoop you will lose weight, lose centimetres, get fit and experience lasting health and fitness results.</p>
    <p class="tight">Our Weight Loss Retreat program is suitable for people of all ages, shapes, sizes and fitness levels. It is amazingly fun and extremely effective with amazing weight loss and fitness results. Whether you want a kick start or are embarking on a long term weight loss program our Weight Loss Retreat program will be one of the best experiences of your life – that's our promise to you.</p>
    <p class="tight">Hundreds of people have already transformed their lives with PineLoop's proven programs. With PineLoop you will lose weight, lose centimetres, get fit and experience lasting health and fitness</p>
  </article>

  <footer>
    <div class="abs footer-links">
      <div class="footer-col"><h3>The Best Programs</h3><ul><li>Weight Loss Retreat</li><li>Residential Boot Camp</li><li>Fitness Days</li><li>At home program</li><li>Local group exercise</li></ul></div>
      <div class="footer-col"><h3>The Best Locations</h3><ul><li>Blue Mountains, NSW</li><li>Sunshine Coast, QLD</li><li>Local Programs</li><li>&nbsp;</li><li>&nbsp;</li></ul></div>
      <div class="footer-col"><h3>About Us</h3><ul><li>Weight Loss Retreat</li><li>Residential Boot Camp</li><li>Fitness Days</li><li>At home program</li><li>Local group exercise</li></ul></div>
      <div class="footer-col"><h3>Results for...</h3><ul><li>Weight Loss</li><li>Fitness goals</li><li>Diabetes reduction</li><li>Blood pressure reduction</li><li>Depression improvement</li><li class="plain">..more health benefits</li></ul></div>
      <div class="footer-col"><h3>FREE Information</h3><ul><li>Request a brochure &gt;&gt;</li><li>FREE PineLoop Magazine</li></ul></div>
    </div>
    <div class="abs footer-bar">
      <span>Contact Us | Book Now | Privacy</span>
      <span>(C) PineLoop Wellbeing PTY Ltd | ABN 5821904736</span>
    </div>
  </footer>
</div>
</body>
</html>
```